Online Rug Store needs Clearance Banner

Website is: Lanternfield Carpets and Home
You can access it at: www.lanternfieldcarpetsandhome.com and login (top right) with password: trazok

*** update: When creating banners for my site, you have permission to use images from www.velbora.com, but ONLY for this project. The images/artwork are copyright allowable for use on www.lanternfieldcarpetsandhome.com projects.***

We need a home page banner sized 1000 wide x 500 tall pixels to promote a "Clearance Sale" on rugs. The banner can state:

1. Clearance Sale
2. Now in progress
3. Save an extra 20% with coupon code 'Mint20'
4. Ends March 31st
5. Plus Free Shipping and 30 day returns.

We prefer a banner that appears hand-drawn and artistic, not commercially produced. It is OK to use a room scene image, rug images, or just a colored/textured background with text and no images. Your choice.

Flat graphics with no shadows and 3-D effect preferred.
Attached is are 3 logo options, as well as an example banner with handcrafted, artistic styling that we prefer.

Target Market(s)

This should be an eye-catching banner to showcase a very urgent promotion. Consider using colors of red, white, gold, and black to make a strong statement on the home page.

Industry/Entity Type

Home And Garden

Requirements
Must have
• Winner must provide Photoshop editable file format (.psd format) including layers that can be edited.
Nice to have
• Hand-drawn, stenciled, scribbled, artistic graphics and fonts is nice because we sell rugs that are made by hand.
Should not have
• little to no shadowing. Avoid computerized graphics.

```html
<!DOCTYPE html>
<html lang="en">
<head>
<meta charset="utf-8">
<title>Lanternfield Carpets and Home — Clearance Sale</title>
<link href="https://fonts.googleapis.com/css2?family=Montserrat:wght@400;500;700;800&family=Oswald:wght@200;300;400&family=Permanent+Marker&display=swap" rel="stylesheet">
<style>
  :root {
    --black: #0b0604;
    --deep-red: #3a0604;
    --rug-red: #8a0f0a;
    --bright-red: #a8160f;
    --clearance-red: #7a0d0c;
    --gold: #ece07f;
    --gold-deep: #b8a449;
    --olive-gold: #8f7a2c;
    --white: #ffffff;
  }
  * { margin: 0; padding: 0; box-sizing: border-box; }
  html, body { width: 1200px; height: 600px; overflow: hidden; background: var(--black); }
  .banner {
    position: relative;
    width: 1200px;
    height: 600px;
    overflow: hidden;
    font-family: "Montserrat", Arial, sans-serif;
    color: var(--white);
  }
  .rug-texture {
    position: absolute; inset: 0;
    background:
      radial-gradient(ellipse at 75% 45%, var(--bright-red) 0%, var(--rug-red) 35%, transparent 75%),
      linear-gradient(90deg, var(--black) 0%, #1a0705 28%, var(--deep-red) 45%, var(--rug-red) 70%, #6e0c08 100%);
  }
  .rug-fringe {
    position: absolute; left: 0; top: 0; width: 90px; height: 600px;
    background: linear-gradient(90deg, rgba(140,100,50,0.45), rgba(60,30,15,0.2) 70%, transparent);
  }
  .brand {
    position: absolute; left: 174px; top: 52px;
    display: flex; align-items: center; gap: 10px;
    font-weight: 500; font-size: 15px; line-height: 1.2;
    color: var(--white);
    background: var(--black);
    padding: 6px 10px;
  }
  .brand-mark { width: 30px; height: 30px; background: var(--bright-red); flex: none; }
  .clearance {
    position: absolute; left: 70px; top: 112px;
    font-family: "Oswald", "Arial Narrow", sans-serif;
    font-weight: 200; font-size: 90px; letter-spacing: 0; line-height: 1;
    color: var(--clearance-red);
    white-space: nowrap;
  }
  .sale-strokes { position: absolute; left: 40px; top: 228px; width: 470px; height: 280px; }
  .sale {
    position: absolute; left: 62px; top: 222px;
    font-family: "Permanent Marker", "Marker Felt", Impact, sans-serif;
    font-size: 176px; line-height: 1;
    color: var(--gold);
    transform: rotate(-9deg);
    transform-origin: left top;
    letter-spacing: -6px;
    white-space: nowrap;
  }
  .ends {
    position: absolute; left: 160px; top: 514px;
    font-family: "Oswald", "Arial Narrow", sans-serif;
    font-weight: 400; font-size: 25px; letter-spacing: 0.5px;
    color: var(--clearance-red);
  }
  .offer { position: absolute; left: 787px; top: 372px; width: 384px; }
  .offer-status { font-weight: 700; font-size: 13px; letter-spacing: 0.3px; margin-left: 7px; }
  .offer-headline { position: relative; height: 108px; }
  .offer-save { position: absolute; left: 3px; top: 8px; font-weight: 800; font-size: 52px; line-height: 1; }
  .offer-extra { position: absolute; left: 3px; top: 70px; font-weight: 500; font-size: 29px; line-height: 1; }
  .offer-percent {
    position: absolute; left: 158px; top: 2px;
    font-weight: 800; font-size: 104px; line-height: 1; letter-spacing: -2px;
    color: var(--olive-gold);
  }
  .offer-code {
    margin-top: 6px; background: var(--black);
    font-weight: 700; font-size: 18px; letter-spacing: 1px;
    padding: 6px 12px; white-space: nowrap;
  }
  .offer-perks { margin-top: 10px; background: var(--black); padding: 6px 12px 10px; }
  .offer-perks-lead { font-weight: 400; font-size: 13px; }
  .offer-perks-main { font-family: "Oswald", "Arial Narrow", sans-serif; font-weight: 300; font-size: 27px; letter-spacing: 0.5px; line-height: 1.1; }
</style>
</head>
<body>
<main class="banner">
  <div class="rug-texture" role="img" aria-label="Close-up photo of a deep red handmade rug pile, fading to black on the left"></div>
  <div class="rug-fringe" role="img" aria-label="Photo of tan rug fringe along the left edge"></div>

  <div class="brand"><span class="brand-mark"></span><span>Lanternfield<br>Carpets and Home</span></div>

  <h1 class="clearance">CLEARANCE</h1>

  <svg class="sale-strokes" viewBox="0 0 470 280" aria-hidden="true">
    <polygon points="6,20 120,0 122,9 8,30" fill="var(--gold-deep)"/>
    <polygon points="20,232 462,118 465,130 24,246" fill="var(--gold)"/>
    <polygon points="60,262 455,160 457,170 64,272" fill="var(--gold-deep)"/>
  </svg>
  <p class="sale">SALE</p>

  <p class="ends">ENDS MARCH 31ST</p>

  <section class="offer">
    <p class="offer-status">NOW IN PROGRESS</p>
    <div class="offer-headline">
      <span class="offer-save">SAVE</span>
      <span class="offer-extra">AN EXTRA</span>
      <span class="offer-percent">20%</span>
    </div>
    <p class="offer-code">WITH COUPON CODE 'MINT20'</p>
    <div class="offer-perks">
      <p class="offer-perks-lead">PLUS FREE</p>
      <p class="offer-perks-main">SHIPPING &amp; 30 DAY RETURNS</p>
    </div>
  </section>
</main>
</body>
</html>
```